Custom Mexican Train Dominos Scorecard

My wife and I regularly play Mexican Train dominos with our friends and family and would like to create a series of custom scorecards specific to our various groups that we play with. The idea would be to have them printed on pads or in notebooks that over time will hold a record of all of our games. Searching around on the web, the only "off the shelf" that I see are pretty plain and boring (see attached). We would love something with a fun and playful mid-century graphic feel to it. Can be a single color or more than one. We want to have the player names incorporated into the design, so for the first one the names would be Tessa, Harold, Ruth & Colin. We will want a place to date each card and of course boxes to fill out the score. I have included a few examples of how the scorecard is basically laid out. Can be any size and can be done in landscape or portrait. I think I would just like the title to say "Domino Night" or potentially no title at all with just a fun domino graphic. Thank you!

Requirements
Must have
• Basic score layout
Nice to have
• nothing in particular
Should not have
• nothing in particular

```html
<!DOCTYPE html>
<html lang="en">
<head>
<meta charset="utf-8">
<title>Domino Night Scorecard</title>
<link rel="stylesheet" href="https://fonts.googleapis.com/css2?family=Bebas+Neue&family=Great+Vibes&display=swap">
<style>
  :root {
    --ink: #151515;
    --rule: #4a4a4a;
    --sheet: rgba(255, 252, 250, 0.74);
    --paint-red: #e8412f;
    --paint-coral: #f07b6b;
    --paint-blush: #f6d9cc;
    --paint-navy: #1d3557;
    --paint-teal: #2a9d8f;
    --paint-deep: #0d4f48;
    --paint-yellow: #efcf3a;
    --badge: #c7bfbd;
  }
  * { margin: 0; padding: 0; box-sizing: border-box; }
  html, body { width: 900px; height: 1200px; overflow: hidden; }
  body { position: relative; font-family: "Bebas Neue", sans-serif; color: var(--ink); }

  .painted-backdrop {
    position: absolute; inset: 0;
    background:
      radial-gradient(circle at 88% 80%, var(--paint-yellow) 0, transparent 22%),
      radial-gradient(circle at 70% 8%, var(--paint-navy) 0, transparent 25%),
      radial-gradient(circle at 8% 85%, var(--paint-teal) 0, transparent 35%),
      linear-gradient(120deg, var(--paint-red) 0%, var(--paint-coral) 28%, var(--paint-blush) 50%, #b9dcd2 68%, var(--paint-deep) 100%);
  }

  .title {
    position: absolute; left: 66px; top: 56px;
    font-size: 58px; letter-spacing: 2px; line-height: 1;
    text-shadow: 2px 2px 0 #fff;
  }

  .date-field {
    position: absolute; left: 617px; top: 60px; width: 218px; height: 43px;
    background: rgba(255, 255, 255, 0.9);
    display: flex; align-items: center; padding-left: 10px;
    font-size: 24px; letter-spacing: 1px;
  }
  .date-field .blanks { margin-left: 12px; letter-spacing: 0; }

  .scorecard {
    position: absolute; left: 66px; top: 134px; width: 768px; height: 1000px;
    background: var(--sheet);
    border-collapse: collapse; table-layout: fixed;
  }
  .scorecard col.label-col { width: 110px; }
  .scorecard tr { height: 66.66px; }
  .scorecard td, .scorecard th {
    border-right: 1px solid var(--rule);
    border-bottom: 1px solid var(--rule);
    text-align: center; vertical-align: middle;
  }
  .scorecard tr > :last-child { border-right: none; }
  .scorecard tr:last-child > * { border-bottom: none; }
  .scorecard .label { border-right: 2px solid var(--ink); }
  .scorecard .player {
    font-family: "Great Vibes", cursive; font-weight: 400;
    font-size: 32px; color: #333;
  }
  .scorecard .total-row td { border-top: 2px solid var(--ink); border-bottom: 2px solid var(--ink); }
  .scorecard .total-row .label, .scorecard .grand-row .label { font-size: 24px; letter-spacing: 0.5px; }
  .scorecard .grand-row td { border-top: 2px solid var(--ink); }

  .host-badge {
    display: inline-block; width: 42px; height: 48px; border-radius: 8px;
    background: var(--badge);
  }

  .domino-column { position: absolute; left: 66px; top: 134px; width: 110px; height: 1000px; pointer-events: none; }
  .domino-column rect { fill: none; stroke: var(--ink); stroke-width: 1.4; }
  .domino-column line { stroke: var(--ink); stroke-width: 1; }
  .domino-column circle { fill: var(--ink); }
</style>
</head>
<body>
  <div class="painted-backdrop" role="img" aria-label="Abstract mid-century painted background in red, coral, teal, navy and yellow"></div>

  <h1 class="title">Domino Night!</h1>
  <div class="date-field">Date <span class="blanks">___/___/___</span></div>

  <table class="scorecard">
    <colgroup><col class="label-col"><col><col><col><col><col><col></colgroup>
    <tr>
      <th class="label"><span class="host-badge" role="img" aria-label="Game host emblem"></span></th>
      <th class="player">Tessa</th><th class="player">Harold</th><th class="player">Ruth</th><th class="player">Colin</th><th></th><th></th>
    </tr>
    <tr><td class="label"></td><td></td><td></td><td></td><td></td><td></td><td></td></tr>
    <tr><td class="label"></td><td></td><td></td><td></td><td></td><td></td><td></td></tr>
    <tr><td class="label"></td><td></td><td></td><td></td><td></td><td></td><td></td></tr>
    <tr><td class="label"></td><td></td><td></td><td></td><td></td><td></td><td></td></tr>
    <tr><td class="label"></td><td></td><td></td><td></td><td></td><td></td><td></td></tr>
    <tr><td class="label"></td><td></td><td></td><td></td><td></td><td></td><td></td></tr>
    <tr class="total-row"><td class="label">Sub Total</td><td></td><td></td><td></td><td></td><td></td><td></td></tr>
    <tr><td class="label"></td><td></td><td></td><td></td><td></td><td></td><td></td></tr>
    <tr><td class="label"></td><td></td><td></td><td></td><td></td><td></td><td></td></tr>
    <tr><td class="label"></td><td></td><td></td><td></td><td></td><td></td><td></td></tr>
    <tr><td class="label"></td><td></td><td></td><td></td><td></td><td></td><td></td></tr>
    <tr><td class="label"></td><td></td><td></td><td></td><td></td><td></td><td></td></tr>
    <tr><td class="label"></td><td></td><td></td><td></td><td></td><td></td><td></td></tr>
    <tr class="grand-row"><td class="label">Game Total</td><td></td><td></td><td></td><td></td><td></td><td></td></tr>
  </table>

  <svg class="domino-column" viewBox="0 0 110 1000" aria-hidden="true">
    <defs>
      <symbol id="pips-1" viewBox="0 0 40 38"><circle cx="20" cy="19" r="2.3"/></symbol>
      <symbol id="pips-2" viewBox="0 0 40 38"><circle cx="10" cy="10" r="2.3"/><circle cx="30" cy="28" r="2.3"/></symbol>
      <symbol id="pips-3" viewBox="0 0 40 38"><circle cx="10" cy="10" r="2.3"/><circle cx="20" cy="19" r="2.3"/><circle cx="30" cy="28" r="2.3"/></symbol>
      <symbol id="pips-4" viewBox="0 0 40 38"><circle cx="11" cy="10" r="2.3"/><circle cx="29" cy="10" r="2.3"/><circle cx="11" cy="28" r="2.3"/><circle cx="29" cy="28" r="2.3"/></symbol>
      <symbol id="pips-5" viewBox="0 0 40 38"><circle cx="11" cy="10" r="2.3"/><circle cx="29" cy="10" r="2.3"/><circle cx="20" cy="19" r="2.3"/><circle cx="11" cy="28" r="2.3"/><circle cx="29" cy="28" r="2.3"/></symbol>
      <symbol id="pips-6" viewBox="0 0 40 38"><circle cx="10" cy="10" r="2.2"/><circle cx="20" cy="10" r="2.2"/><circle cx="30" cy="10" r="2.2"/><circle cx="10" cy="28" r="2.2"/><circle cx="20" cy="28" r="2.2"/><circle cx="30" cy="28" r="2.2"/></symbol>
      <symbol id="pips-7" viewBox="0 0 40 38"><circle cx="10" cy="10" r="2.2"/><circle cx="20" cy="10" r="2.2"/><circle cx="30" cy="10" r="2.2"/><circle cx="20" cy="19" r="2.2"/><circle cx="10" cy="28" r="2.2"/><circle cx="20" cy="28" r="2.2"/><circle cx="30" cy="28" r="2.2"/></symbol>
      <symbol id="pips-8" viewBox="0 0 40 38"><circle cx="10" cy="10" r="2.2"/><circle cx="20" cy="10" r="2.2"/><circle cx="30" cy="10" r="2.2"/><circle cx="15" cy="19" r="2.2"/><circle cx="25" cy="19" r="2.2"/><circle cx="10" cy="28" r="2.2"/><circle cx="20" cy="28" r="2.2"/><circle cx="30" cy="28" r="2.2"/></symbol>
      <symbol id="pips-9" viewBox="0 0 40 38"><circle cx="10" cy="10" r="2.2"/><circle cx="20" cy="10" r="2.2"/><circle cx="30" cy="10" r="2.2"/><circle cx="10" cy="19" r="2.2"/><circle cx="20" cy="19" r="2.2"/><circle cx="30" cy="19" r="2.2"/><circle cx="10" cy="28" r="2.2"/><circle cx="20" cy="28" r="2.2"/><circle cx="30" cy="28" r="2.2"/></symbol>
      <symbol id="pips-10" viewBox="0 0 40 38"><circle cx="8" cy="10" r="2.1"/><circle cx="16" cy="10" r="2.1"/><circle cx="24" cy="10" r="2.1"/><circle cx="32" cy="10" r="2.1"/><circle cx="12" cy="19" r="2.1"/><circle cx="28" cy="19" r="2.1"/><circle cx="8" cy="28" r="2.1"/><circle cx="16" cy="28" r="2.1"/><circle cx="24" cy="28" r="2.1"/><circle cx="32" cy="28" r="2.1"/></symbol>
      <symbol id="pips-11" viewBox="0 0 40 38"><circle cx="8" cy="10" r="2.1"/><circle cx="16" cy="10" r="2.1"/><circle cx="24" cy="10" r="2.1"/><circle cx="32" cy="10" r="2.1"/><circle cx="12" cy="19" r="2.1"/><circle cx="20" cy="19" r="2.1"/><circle cx="28" cy="19" r="2.1"/><circle cx="8" cy="28" r="2.1"/><circle cx="16" cy="28" r="2.1"/><circle cx="24" cy="28" r="2.1"/><circle cx="32" cy="28" r="2.1"/></symbol>
      <symbol id="pips-12" viewBox="0 0 40 38"><circle cx="8" cy="10" r="2.1"/><circle cx="16" cy="10" r="2.1"/><circle cx="24" cy="10" r="2.1"/><circle cx="32" cy="10" r="2.1"/><circle cx="8" cy="19" r="2.1"/><circle cx="16" cy="19" r="2.1"/><circle cx="24" cy="19" r="2.1"/><circle cx="32" cy="19" r="2.1"/><circle cx="8" cy="28" r="2.1"/><circle cx="16" cy="28" r="2.1"/><circle cx="24" cy="28" r="2.1"/><circle cx="32" cy="28" r="2.1"/></symbol>
      <g id="domino-frame"><rect x="0" y="0" width="81" height="38" rx="6"/><line x1="40.5" y1="0" x2="40.5" y2="38"/></g>
    </defs>

    <g transform="translate(14.5 81)"><use href="#domino-frame"/><use href="#pips-1" width="40" height="38"/><use href="#pips-1" x="40.5" width="40" height="38"/></g>
    <g transform="translate(14.5 147.7)"><use href="#domino-frame"/><use href="#pips-2" width="40" height="38"/><use href="#pips-2" x="40.5" width="40" height="38"/></g>
    <g transform="translate(14.5 214.3)"><use href="#domino-frame"/><use href="#pips-3" width="40" height="38"/><use href="#pips-3" x="40.5" width="40" height="38"/></g>
    <g transform="translate(14.5 281)"><use href="#domino-frame"/><use href="#pips-4" width="40" height="38"/><use href="#pips-4" x="40.5" width="40" height="38"/></g>
    <g transform="translate(14.5 347.7)"><use href="#domino-frame"/><use href="#pips-5" width="40" height="38"/><use href="#pips-5" x="40.5" width="40" height="38"/></g>
    <g transform="translate(14.5 414.3)"><use href="#domino-frame"/><use href="#pips-6" width="40" height="38"/><use href="#pips-6" x="40.5" width="40" height="38"/></g>

    <g transform="translate(14.5 547.7)"><use href="#domino-frame"/><use href="#pips-7" width="40" height="38"/><use href="#pips-7" x="40.5" width="40" height="38"/></g>
    <g transform="translate(14.5 614.3)"><use href="#domino-frame"/><use href="#pips-8" width="40" height="38"/><use href="#pips-8" x="40.5" width="40" height="38"/></g>
    <g transform="translate(14.5 681)"><use href="#domino-frame"/><use href="#pips-9" width="40" height="38"/><use href="#pips-9" x="40.5" width="40" height="38"/></g>
    <g transform="translate(14.5 747.7)"><use href="#domino-frame"/><use href="#pips-10" width="40" height="38"/><use href="#pips-10" x="40.5" width="40" height="38"/></g>
    <g transform="translate(14.5 814.3)"><use href="#domino-frame"/><use href="#pips-11" width="40" height="38"/><use href="#pips-11" x="40.5" width="40" height="38"/></g>
    <g transform="translate(14.5 881)"><use href="#domino-frame"/><use href="#pips-12" width="40" height="38"/><use href="#pips-12" x="40.5" width="40" height="38"/></g>
  </svg>
</body>
</html>
```